Stationary for Vornik Consulting

Hi

I am after stationary designs for my company - Vornik Consulting. I have a logo - recently designed by PixelHarbor. Vornik ( sales spelt backwards ) is a sales consultancy - including sales training, sales coaching and business management.

I have attached some of the artwork I already have, as well as a few ideas
1. Use supplied logo's
2. back of business card to use the logo with the dark background and white text
3. details to be included on card are
Logo
Delmo Kastrani
p: +61409371826
e: delmo@vornikconsulting.com.au
w: www.vornikconsulting.com.au
PO Box 417, Balwyn North, Victoria, 3104

4. I am after designs for business cards, A4 letterhead and A5 letterhead

Thanks in Advance

Delmo

```html
<!DOCTYPE html>
<html lang="en">
<head>
<meta charset="utf-8">
<title>Vornik Consulting — Stationery</title>
<link href="https://fonts.googleapis.com/css2?family=Montserrat:wght@400;500;600;700;800&display=swap" rel="stylesheet">
<style>
  :root {
    --board: #2a2a2a;
    --slate: #334653;
    --ink: #2f3e48;
    --orange: #d4472a;
    --orange-text: #e0532f;
    --paper: #ffffff;
    --muted: #5b6168;
    --faint: #eceeef;
    --label: #ffffff;
  }
  * { margin: 0; padding: 0; box-sizing: border-box; }
  html, body { width: 1200px; height: 900px; overflow: hidden; }
  body {
    position: relative;
    background: var(--board);
    font-family: "Montserrat", sans-serif;
  }
  .item-label {
    position: absolute;
    color: var(--label);
    font-weight: 700;
    font-size: 14px;
    letter-spacing: 0.2px;
    text-align: center;
    transform: translateX(-50%);
    white-space: nowrap;
  }
  .sheet, .card {
    position: absolute;
    overflow: hidden;
    box-shadow: 0 2px 6px rgba(0,0,0,0.45);
  }
  .sheet { background: var(--paper); }
  .brand {
    font-weight: 700;
    white-space: nowrap;
    letter-spacing: 0.3px;
    line-height: 1;
  }
  .brand-dark { color: var(--ink); }
  .brand-light { color: var(--paper); }

  /* letterheads */
  .lh-header { position: absolute; display: flex; }
  .lh-contact { display: flex; gap: 12px; color: var(--muted); line-height: 1.3; }
  .lh-contact .row { display: flex; align-items: flex-start; gap: 3px; }
  .lh-watermark {
    position: absolute; left: 0; white-space: nowrap;
    font-weight: 800; color: var(--faint); line-height: 1;
  }
  .icon { flex: none; fill: var(--orange-text); margin-top: 1px; }

  /* card fronts */
  .card-front { display: flex; flex-direction: column; align-items: center; justify-content: center; }
  .card-front .brand { font-size: 17px; margin-top: -6px; }
  .card-front .web {
    position: absolute; bottom: 8px; left: 0; right: 0; text-align: center;
    color: var(--paper); font-size: 5.5px; font-weight: 500;
  }
  .front-slate { background: var(--slate); }
  .front-orange { background: var(--orange); }
  .round-a { border-radius: 18px 0 18px 0; }
  .round-b { border-radius: 0 22px 0 22px; }

  /* card backs */
  .card-back { background: var(--paper); color: var(--muted); font-size: 5px; }
  .back-wide .brand { position: absolute; left: 15px; top: 28px; font-size: 13px; }
  .back-wide .person {
    position: absolute; right: 12px; top: 68px;
    color: var(--orange-text); font-size: 7.5px; font-weight: 600;
  }
  .back-wide .rule { position: absolute; left: 12px; right: 12px; top: 80px; height: 1px; background: #f2b7a7; }
  .back-wide .details { position: absolute; left: 14px; right: 12px; top: 86px; display: flex; justify-content: space-between; }
  .details .col { display: flex; flex-direction: column; gap: 4px; }
  .details .row { display: flex; gap: 3px; align-items: flex-start; line-height: 1.25; }

  .back-split .brand {
    position: absolute; left: 14px; top: 47px; width: 76px;
    font-size: 11px; line-height: 1.2; white-space: normal;
  }
  .back-split .divider { position: absolute; left: 98px; top: 22px; bottom: 22px; width: 1px; background: #d9d9d9; }
  .back-split .info { position: absolute; left: 108px; top: 30px; display: flex; flex-direction: column; gap: 3px; }
  .back-split .person { color: var(--orange-text); font-size: 7px; font-weight: 600; margin-bottom: 4px; }
  .back-split .row { display: flex; gap: 3px; line-height: 1.25; }
</style>
</head>
<body>

<svg width="0" height="0" style="position:absolute">
  <defs>
    <symbol id="i-pin" viewBox="0 0 10 10"><path d="M5 0a3.5 3.5 0 0 0-3.5 3.5C1.5 6 5 10 5 10s3.5-4 3.5-6.5A3.5 3.5 0 0 0 5 0zm0 5a1.5 1.5 0 1 1 0-3 1.5 1.5 0 0 1 0 3z"/></symbol>
    <symbol id="i-phone" viewBox="0 0 10 10"><path d="M1 3c0-1 1-2 4-2s4 1 4 2v1H7V3H3v1H1zM2 5h6l1 4H1z"/></symbol>
    <symbol id="i-mail" viewBox="0 0 10 10"><path d="M0 2h10v6H0zM1 3l4 3 4-3"/></symbol>
    <symbol id="i-web" viewBox="0 0 10 10"><circle cx="5" cy="5" r="4.5"/></symbol>
  </defs>
</svg>

<!-- A4 letterhead -->
<div class="item-label" style="left:200px; top:132px;">A4-LETTERHEAD</div>
<div class="sheet a4" style="left:18px; top:162px; width:387px; height:549px;">
  <div class="lh-header" style="left:30px; top:42px;">
    <div class="brand brand-dark" style="font-size:14px; margin-top:8px;">Vornik Consulting</div>
  </div>
  <div class="lh-header lh-contact" style="left:188px; top:44px; font-size:6.5px;">
    <div class="row"><svg class="icon" width="6" height="6"><use href="#i-pin"/></svg><span>PO Box 417,<br>Balwyn North,<br>Victoria, 3104</span></div>
    <div>
      <div class="row"><svg class="icon" width="6" height="6"><use href="#i-phone"/></svg>+61409371826</div>
      <div class="row"><svg class="icon" width="6" height="6"><use href="#i-mail"/></svg>delmo@vornikconsulting.com.au</div>
      <div class="row"><svg class="icon" width="6" height="6"><use href="#i-web"/></svg>www.vornikconsulting.com.au</div>
    </div>
  </div>
  <div class="lh-watermark" style="top:462px; font-size:88px;">Vornik</div>
</div>

<!-- A5 letterhead -->
<div class="item-label" style="left:563px; top:45px;">A5-LETTERHEAD</div>
<div class="sheet a5" style="left:413px; top:92px; width:313px; height:442px;">
  <div class="lh-header" style="left:24px; top:40px;">
    <div class="brand brand-dark" style="font-size:11px;">Vornik Consulting</div>
  </div>
  <div class="lh-header lh-contact" style="left:152px; top:35px; font-size:5.3px;">
    <div class="row"><svg class="icon" width="5" height="5"><use href="#i-pin"/></svg><span>PO Box 417,<br>Balwyn North,<br>Victoria, 3104</span></div>
    <div>
      <div class="row"><svg class="icon" width="5" height="5"><use href="#i-phone"/></svg>+61409371826</div>
      <div class="row"><svg class="icon" width="5" height="5"><use href="#i-mail"/></svg>delmo@vornikconsulting.com.au</div>
      <div class="row"><svg class="icon" width="5" height="5"><use href="#i-web"/></svg>www.vornikconsulting.com.au</div>
    </div>
  </div>
  <div class="lh-watermark" style="top:372px; font-size:72px;">Vornik</div>
</div>

<!-- Back 1 & 2 -->
<div class="item-label" style="left:845px; top:44px;">BACK-1</div>
<div class="card card-back back-wide" style="left:738px; top:68px; width:215px; height:122px;">
  <div class="brand brand-dark">Vornik Consulting</div>
  <div class="person">Delmo Kastrani</div>
  <div class="rule"></div>
  <div class="details">
    <div class="col">
      <div class="row"><svg class="icon" width="5" height="5"><use href="#i-pin"/></svg><span>PO Box 417,<br>Balwyn North, Victoria, 3104</span></div>
      <div class="row"><svg class="icon" width="5" height="5"><use href="#i-mail"/></svg>delmo@vornikconsulting.com.au</div>
    </div>
    <div class="col">
      <div class="row"><svg class="icon" width="5" height="5"><use href="#i-phone"/></svg>+61409371826</div>
      <div class="row"><svg class="icon" width="5" height="5"><use href="#i-web"/></svg>www.vornikconsulting.com.au</div>
    </div>
  </div>
</div>

<div class="item-label" style="left:1075px; top:44px;">BACK-2</div>
<div class="card card-back back-wide round-b" style="left:967px; top:68px; width:216px; height:122px;">
  <div class="brand brand-dark">Vornik Consulting</div>
  <div class="person">Delmo Kastrani</div>
  <div class="rule"></div>
  <div class="details">
    <div class="col">
      <div class="row"><svg class="icon" width="5" height="5"><use href="#i-pin"/></svg><span>PO Box 417,<br>Balwyn North, Victoria, 3104</span></div>
      <div class="row"><svg class="icon" width="5" height="5"><use href="#i-mail"/></svg>delmo@vornikconsulting.com.au</div>
    </div>
    <div class="col">
      <div class="row"><svg class="icon" width="5" height="5"><use href="#i-phone"/></svg>+61409371826</div>
      <div class="row"><svg class="icon" width="5" height="5"><use href="#i-web"/></svg>www.vornikconsulting.com.au</div>
    </div>
  </div>
</div>

<!-- Fronts 1-4 -->
<div class="item-label" style="left:846px; top:199px;">FRONT-1</div>
<div class="card card-front front-slate" style="left:737px; top:219px; width:218px; height:125px;">
  <div class="brand brand-light">Vornik Consulting</div>
  <div class="web">www.vornikconsulting.com.au</div>
</div>

<div class="item-label" style="left:1074px; top:197px;">FRONT-2</div>
<div class="card card-front front-slate round-a" style="left:966px; top:219px; width:217px; height:125px;">
  <div class="brand brand-light">Vornik Consulting</div>
  <div class="web">www.vornikconsulting.com.au</div>
</div>

<div class="item-label" style="left:850px; top:360px;">FRONT-3</div>
<div class="card card-front front-slate" style="left:741px; top:386px; width:215px; height:122px;">
  <div class="brand brand-light">Vornik Consulting</div>
  <div class="web">www.vornikconsulting.com.au</div>
</div>

<div class="item-label" style="left:1075px; top:358px;">FRONT-4</div>
<div class="card card-front front-slate round-a" style="left:967px; top:386px; width:216px; height:120px;">
  <div class="brand brand-light">Vornik Consulting</div>
  <div class="web">www.vornikconsulting.com.au</div>
</div>

<!-- Front 5, Back 3 & 4 -->
<div class="item-label" style="left:613px; top:545px;">FRONT-5</div>
<div class="card card-front front-orange" style="left:507px; top:573px; width:213px; height:121px;">
  <div class="brand brand-light">Vornik Consulting</div>
  <div class="web">www.vornikconsulting.com.au</div>
</div>

<div class="item-label" style="left:848px; top:542px;">BACK-3</div>
<div class="card card-back back-split" style="left:742px; top:574px; width:213px; height:120px;">
  <div class="brand brand-dark">Vornik<br>Consulting</div>
  <div class="divider"></div>
  <div class="info">
    <div class="person">Delmo Kastrani</div>
    <div class="row">PO Box 417,<br>Balwyn North, Victoria, 3104</div>
    <div class="row"><svg class="icon" width="5" height="5"><use href="#i-phone"/></svg>+61409371826</div>
    <div class="row"><svg class="icon" width="5" height="5"><use href="#i-mail"/></svg>delmo@vornikconsulting.com.au</div>
    <div class="row"><svg class="icon" width="5" height="5"><use href="#i-web"/></svg>www.vornikconsulting.com.au</div>
  </div>
</div>

<div class="item-label" style="left:1075px; top:542px;">BACK-4</div>
<div class="card card-back back-split round-b" style="left:968px; top:574px; width:216px; height:122px;">
  <div class="brand brand-dark">Vornik<br>Consulting</div>
  <div class="divider"></div>
  <div class="info">
    <div class="person">Delmo Kastrani</div>
    <div class="row">PO Box 417,<br>Balwyn North, Victoria, 3104</div>
    <div class="row"><svg class="icon" width="5" height="5"><use href="#i-phone"/></svg>+61409371826</div>
    <div class="row"><svg class="icon" width="5" height="5"><use href="#i-mail"/></svg>delmo@vornikconsulting.com.au</div>
    <div class="row"><svg class="icon" width="5" height="5"><use href="#i-web"/></svg>www.vornikconsulting.com.au</div>
  </div>
</div>

<!-- Fronts 6-8 -->
<div class="item-label" style="left:613px; top:714px;">FRONT-6</div>
<div class="card card-front front-orange round-a" style="left:507px; top:740px; width:213px; height:120px;">
  <div class="brand brand-light">Vornik Consulting</div>
  <div class="web">www.vornikconsulting.com.au</div>
</div>

<div class="item-label" style="left:850px; top:714px;">FRONT-7</div>
<div class="card card-front front-orange" style="left:744px; top:739px; width:212px; height:119px;">
  <div class="brand brand-light">Vornik Consulting</div>
  <div class="web">www.vornikconsulting.com.au</div>
</div>

<div class="item-label" style="left:1075px; top:714px;">FRONT-8</div>
<div class="card card-front front-orange round-a" style="left:972px; top:739px; width:211px; height:119px;">
  <div class="brand brand-light">Vornik Consulting</div>
  <div class="web">www.vornikconsulting.com.au</div>
</div>

</body>
</html>
```